Moltbeck Chardonnay Wine Label 2024

We need a wine label design for a small, family-owned vineyard in Broke, Hunter Valley of NSW (Australia). The vineyard is called Moltbeck and we have an existing logo and 'brand book' for the vineyard home that is rented out for short stay bookings. This is attached and includes font style, colour palette and our Moltbeck logo for the accommodation (we're not wedded to this but also probably not after a completely different rethink either as we want the accommodation and the wine to feel part of the same thing.

Project:
The initial label requirement (front and back) is for the Moltbeck 2024 Chardonnay, which is called 'Juniper'. The label would need to be able to extend to other varietals (eg Verdehlo and Sparkling) in 2025. Attached is draft copy for front and back for the 2024 Chardonnay as a guide.

STYLE: We like a relatively simple, classic design and have played with both a dark (navy) and a light background (white/cream). Based on the final label design we will order a Kortap colour to pick up on the label theme.

The Chardonnay bottle dimensions are attached, as is our logo file (if that helps)

online 25-50 yearold

Wine

• front and back label design Moltbeck logo and name

```html
<!DOCTYPE html>
<html lang="en">
<head>
<meta charset="utf-8">
<title>Moltbeck Juniper Chardonnay 2024 – Label</title>
<link rel="stylesheet" href="https://fonts.googleapis.com/css2?family=Merriweather:wght@700&family=Gloock&family=Raleway:wght@300;400&display=swap">
<style>
  :root {
    --backdrop: #c4c4c4;
    --paper: #f5f7f6;
    --paper-shade: #e6ebe9;
    --navy: #1b2030;
    --navy-soft: #4a5163;
    --art-light: #d9dcdf;
    --art-mid: #8a909c;
  }
  * { margin: 0; padding: 0; box-sizing: border-box; }
  html, body {
    width: 1183px;
    height: 1200px;
    overflow: hidden;
    background: var(--backdrop);
  }
  .canvas {
    position: relative;
    width: 1183px;
    height: 1200px;
  }
  /* Neck label */
  .neck-label {
    position: absolute;
    left: 80px;
    top: 80px;
    width: 210px;
    height: 256px;
    background: linear-gradient(90deg, var(--paper-shade), var(--paper) 25%, var(--paper) 75%, var(--paper-shade));
    display: flex;
    flex-direction: column;
    align-items: center;
    justify-content: center;
    gap: 14px;
  }
  .neck-label .brand-dot {
    width: 34px;
    height: 34px;
    border-radius: 50%;
    background: var(--navy);
  }
  .neck-label .brand-name {
    font-family: "Merriweather", Georgia, serif;
    font-weight: 700;
    font-size: 30px;
    color: var(--navy);
  }
  /* Front label */
  .front-label {
    position: absolute;
    left: 380px;
    top: 80px;
    width: 700px;
    height: 1040px;
    background: linear-gradient(90deg, var(--paper-shade), var(--paper) 12%, var(--paper) 88%, var(--paper-shade));
  }
  .ornament-band {
    position: absolute;
    left: 0;
    top: 18px;
    width: 700px;
    height: 72px;
    border-top: 3px solid var(--navy);
    border-bottom: 3px solid var(--navy);
  }
  .ornament-band .pattern {
    position: absolute;
    left: 0;
    top: 9px;
    width: 100%;
    height: 48px;
    background: linear-gradient(90deg, var(--navy-soft), var(--art-mid), var(--navy-soft));
  }
  .brand-line {
    position: absolute;
    left: 0;
    top: 196px;
    width: 100%;
    display: flex;
    justify-content: center;
    align-items: center;
    gap: 14px;
  }
  .brand-line .brand-name {
    font-family: "Merriweather", Georgia, serif;
    font-weight: 700;
    font-size: 46px;
    color: var(--navy);
  }
  .brand-line .brand-dot {
    width: 30px;
    height: 30px;
    border-radius: 50%;
    background: var(--navy);
    margin-top: -30px;
  }
  .wine-name {
    position: absolute;
    left: 0;
    top: 290px;
    width: 100%;
    text-align: center;
    font-family: "Gloock", "Bodoni Moda", serif;
    font-size: 116px;
    line-height: 1;
    letter-spacing: 1px;
    color: var(--navy);
  }
  .varietal {
    position: absolute;
    left: 0;
    top: 410px;
    width: 100%;
    text-align: center;
    font-family: "Raleway", Arial, sans-serif;
    font-weight: 300;
    font-size: 36px;
    letter-spacing: 1px;
    color: var(--navy);
  }
  .region-art {
    position: absolute;
    left: 115px;
    top: 505px;
    width: 477px;
    height: 370px;
    border-radius: 48% 48% 20% 20% / 30% 30% 14% 14%;
    background: radial-gradient(ellipse at 50% 45%, var(--art-light), var(--art-mid) 70%, var(--navy-soft));
  }
  .volume {
    position: absolute;
    left: 0;
    top: 905px;
    width: 100%;
    text-align: center;
    font-family: "Raleway", Arial, sans-serif;
    font-weight: 400;
    font-size: 30px;
    color: var(--navy);
  }
  .base-rule {
    position: absolute;
    left: 0;
    width: 100%;
    background: var(--navy);
  }
  .base-rule.thick { top: 980px; height: 12px; }
  .base-rule.thin { top: 1016px; height: 5px; }
</style>
</head>
<body>
<main class="canvas">
  <section class="neck-label">
    <span class="brand-dot"></span>
    <span class="brand-name">Moltbeck</span>
  </section>

  <section class="front-label">
    <div class="ornament-band">
      <div class="pattern" role="img" aria-label="Decorative floral border pattern"></div>
    </div>

    <div class="brand-line">
      <span class="brand-name">Moltbeck</span>
      <span class="brand-dot"></span>
    </div>

    <h1 class="wine-name">JUNIPER</h1>
    <p class="varietal">Chardonnay 2024</p>

    <div class="region-art" role="img" aria-label="Engraved crest of Hunter Valley vineyard rows, hills, rising sun and a bird in flight, with a Hunter Valley banner"></div>

    <p class="volume">750ml</p>

    <div class="base-rule thick"></div>
    <div class="base-rule thin"></div>
  </section>
</main>
</body>
</html>
```